Home Design company focused on remodel and enhancement of kitchens and bathroorms

I already have a logo designed by ArtHarbor, I now need a design for my business cards.
The company is in the remodeling and enhancement industry for homes, focusing on kitchens and bathrooms, however, we can remodel or enhance every room in a home, an office space, etc.

The company's name is VELMOR HOME DESIGN, LLC

We'll focus on clients in the Rio Grande Valley, Texas. Primarily McAllen, Edinburg, Pharr, Mission, Brownsville and South Padre Island.

The design on the business card should transmit reliability, professionalism anda bit of upscale design.

The logo is in black and white, and would like to keep it that way.

The information that needs to be printed in the business cards is:
Company's name: Velmor Home Design
Company's Logo (attached)
My name: Noel Bramwit
Address, phone and email:
2715 N Parkline Road, Ste 348
Harlow Bend, TX 78090
(361) 555 0187
nbramwit@velmordesign.example
Website: velmordesign.example

```html
<!DOCTYPE html>
<html lang="en">
<head>
<meta charset="utf-8">
<title>Velmor Home Design – Business Card</title>
<link rel="stylesheet" href="https://fonts.googleapis.com/css2?family=Jost:wght@400;500;600&display=swap">
<style>
  :root {
    --backdrop: #cbcbcb;
    --card-front: #ffffff;
    --card-back: #050505;
    --ink: #0d0d0d;
    --pattern-dark: #1c1f1f;
    --pattern-mid: #3a403f;
  }
  * { margin: 0; padding: 0; box-sizing: border-box; }
  html, body {
    width: 1200px; height: 846px; overflow: hidden;
    background: var(--backdrop);
    font-family: "Jost", sans-serif;
    color: var(--ink);
  }
  .canvas { position: relative; width: 1200px; height: 846px; }

  .card {
    position: absolute;
    left: 346px;
    width: 508px;
    height: 290px;
  }
  .card--front { top: 113px; background: var(--card-front); }
  .card--back {
    top: 443px;
    background:
      radial-gradient(ellipse at 50% 50%, var(--pattern-mid) 0%, var(--pattern-dark) 45%, var(--card-back) 80%);
  }

  .brand-name {
    position: absolute;
    left: 472px; top: 263px;
    transform: translate(-50%, -50%) rotate(-90deg);
    white-space: nowrap;
    font-size: 10.5px;
    font-weight: 400;
    letter-spacing: 1.4px;
    color: var(--ink);
  }
  .divider {
    position: absolute;
    left: 511px; top: 203px;
    width: 1px; height: 121px;
    background: var(--ink);
  }

  .contact-name {
    position: absolute;
    left: 561px; top: 200px;
    font-size: 18.5px;
    font-weight: 600;
    line-height: 1;
  }
  .contact-line {
    position: absolute;
    left: 561px;
    font-size: 12.6px;
    font-weight: 400;
    line-height: 16px;
    white-space: nowrap;
  }
  .contact-line--phone { top: 230px; }
  .contact-line--email { top: 251px; }
  .contact-line--web { top: 271px; }
  .contact-line--address { top: 297px; }

  .icon { position: absolute; fill: var(--ink); }
  .icon--phone { left: 541px; top: 228px; width: 11px; height: 19px; }
  .icon--email { left: 538px; top: 253px; width: 17px; height: 12px; }
  .icon--web { left: 538px; top: 270px; width: 18px; height: 18px; }
  .icon--pin { left: 538px; top: 299px; width: 17px; height: 25px; }
</style>
</head>
<body>
<main class="canvas">

  <section class="card card--front" aria-label="Business card front"></section>

  <div class="brand-name">VELMOR HOME DESIGN</div>
  <div class="divider"></div>

  <h1 class="contact-name">Noel Bramwit</h1>

  <svg class="icon icon--phone" viewBox="0 0 11 19" aria-hidden="true">
    <path d="M2 0h7a2 2 0 0 1 2 2v15a2 2 0 0 1-2 2H2a2 2 0 0 1-2-2V2a2 2 0 0 1 2-2zm-.6 3v12h8.2V3zM4 1.2v.8h3v-.8zm1.5 15.2a.9.9 0 1 0 0 1.8.9.9 0 0 0 0-1.8z"/>
  </svg>
  <p class="contact-line contact-line--phone">(361) 555 0187</p>

  <svg class="icon icon--email" viewBox="0 0 17 12" aria-hidden="true">
    <path d="M0 0h17v12H0zM1.2 1.2l7.3 5.6 7.3-5.6zM1 2.3v8.2l5-4.4zm15 0L11 6.1l5 4.4zM6.8 6.7 1.6 11h13.8l-5.2-4.3-1.7 1.3z"/>
  </svg>
  <p class="contact-line contact-line--email">nbramwit@velmordesign.example</p>

  <svg class="icon icon--web" viewBox="0 0 18 18" aria-hidden="true">
    <circle cx="9" cy="9" r="9"/>
    <g fill="none" stroke="#fff" stroke-width="0.9">
      <ellipse cx="9" cy="9" rx="3.6" ry="8.6"/>
      <line x1="9" y1="0.4" x2="9" y2="17.6"/>
      <line x1="0.4" y1="9" x2="17.6" y2="9"/>
      <path d="M2 4.6h14M2 13.4h14"/>
    </g>
  </svg>
  <p class="contact-line contact-line--web">www.velmordesign.example</p>

  <svg class="icon icon--pin" viewBox="0 0 17 25" aria-hidden="true">
    <path d="M8.5 0A8.5 8.5 0 0 0 0 8.5C0 14.5 8.5 25 8.5 25S17 14.5 17 8.5A8.5 8.5 0 0 0 8.5 0zm0 5a3.4 3.4 0 1 1 0 6.8 3.4 3.4 0 0 1 0-6.8z"/>
  </svg>
  <p class="contact-line contact-line--address">2715 N Parkline Road, Ste 348<br>Harlow Bend, TX 78090</p>

  <section class="card card--back" role="img" aria-label="Repeating brand pattern in soft grey on a black card back"></section>

</main>
</body>
</html>
```